Brandlark CEO needs a Crowdsourced Graphic for a Gizmoreel Article

I need a simple graphic / banner for a blog post that's going to be posted on Gizmoreel (www.gizmoreel.example) - the biggest tech blog in the world.

The article will be written by Omar Feltz (Brandlark's CEO) and the title will be "The Quiet Harbor Surge Unveiled". The article is about the tens of thousands of people using crowdsourcing websites (like Brandlark.example, Qtaskly.example and Wervo.example) in China, India, the Philippines, Australia and other countries in the Asia Pacific region.

We'd really like to get this ASAP - so early submissions encouraged. We will try and get the winning designer linked to from the article.
Updates

Thanks to everyone that submitted!  Some great designs and hard to choose! :)

Target Market(s)

Tech saavy readers, English speakers

Industry/Entity Type

Tech

Requirements
Must have
• The graphic SHOULD:
1) Have the text "The quiet harbor surge unveiled" with some nice design and fonts (consider grey subtle pattern background and white drop shadow on fonts) - see attached examples
2) Have an Asian theme
3) Have the dimensions 640px wide by 240px wide
Nice to have
• The graphic COULD:
1) Have references to some or all of the countries mentioned above or use Asian characters as part of the background / motif (maybe the word "crowd" or "crowd sourcing" in different languages). In Chinese, the word for crowdsourcing is "witkey" (and there are corresponding Chinese characters: ??)
2) Emphasize the word "Asia" (using color and larger/different font)
3) Use a chart showing exponential (i.e. fast) growth - like the attached
4) Have a second line of text "7 Odd Facts Hiding Behind the Quiet Harbor Surge"

```html
<!DOCTYPE html>
<html lang="en">
<head>
<meta charset="utf-8">
<title>BL Gizmoreel Banner – Presentation Sheet</title>
<link rel="stylesheet" href="https://fonts.googleapis.com/css2?family=Bebas+Neue&family=Arimo:wght@400&display=swap">
<style>
  :root {
    --sheet: #ffffff;
    --rule: #c9c9c9;
    --ink: #1c1c1c;
    --banner-bg: #e7e7e7;
    --banner-shade: #d5d5d5;
    --headline: #3a3a3a;
    --accent: #1a8f3c;
    --chart-line: #555555;
    --node-ring: #ffffff;
    --map-tint-a: #9fd0ad;
    --map-tint-b: #c6e3ce;
  }
  * { margin: 0; padding: 0; box-sizing: border-box; }
  html, body { width: 1200px; height: 1000px; overflow: hidden; background: var(--sheet); }
  body { position: relative; font-family: "Arimo", Arial, sans-serif; color: var(--ink); }

  .sheet-header {
    position: absolute; left: 55px; top: 0; width: 1097px; height: 117px;
    border-bottom: 1px solid var(--rule);
  }
  .header-divider { position: absolute; top: 25px; width: 1px; height: 92px; background: var(--rule); }
  .header-divider.first { left: 323px; }
  .header-divider.second { left: 626px; }
  .header-field { position: absolute; top: 47px; font-size: 14px; line-height: 19px; letter-spacing: 0.6px; }
  .header-field .field-label { text-transform: uppercase; }
  .header-field.project { left: 378px; }
  .header-field.completed { left: 688px; }

  .banner-frame { position: absolute; left: 119px; overflow: hidden; }
  .banner-frame.large { top: 187px; width: 960px; height: 360px; }
  .banner-frame.actual { top: 630px; width: 640px; height: 240px; }
  .banner {
    position: absolute; left: 0; top: 0; width: 960px; height: 360px;
    background: var(--banner-bg); transform-origin: 0 0;
  }
  .banner-frame.actual .banner { transform: scale(0.6667); }
  .banner-art { position: absolute; left: 0; top: 0; }

  .headline {
    position: absolute; left: 52px; top: 56px;
    font-family: "Bebas Neue", "Oswald", sans-serif;
    font-size: 74px; line-height: 70px; color: var(--headline);
    letter-spacing: 1px; text-shadow: 1px 1px 0 #ffffff;
    white-space: nowrap;
  }
  .headline .emphasis { color: var(--accent); }
  .subline {
    position: absolute; left: 55px; top: 210px;
    font-family: "Bebas Neue", "Oswald", sans-serif;
    font-size: 31px; line-height: 38px; color: var(--headline);
    letter-spacing: 1.2px; text-shadow: 1px 1px 0 #ffffff;
    white-space: nowrap;
  }

  .caption { position: absolute; left: 119px; font-size: 13px; letter-spacing: 0.3px; }
  .caption.large { top: 566px; }
  .caption.actual { top: 895px; }
</style>
</head>
<body>

<header class="sheet-header">
  <div class="header-divider first"></div>
  <div class="header-divider second"></div>
  <div class="header-field project">
    <div class="field-label">Project Title:</div>
    <div class="field-value">BL Gizmoreel Banner</div>
  </div>
  <div class="header-field completed">
    <div class="field-label">Date of Completion:</div>
    <div class="field-value">21-NOV-2012</div>
  </div>
</header>

<div class="banner-frame large">
  <div class="banner">
    <svg class="banner-art" width="960" height="360" viewBox="0 0 960 360">
      <defs>
        <linearGradient id="mapTint" x1="0" y1="0" x2="1" y2="1">
          <stop offset="0" stop-color="var(--map-tint-a)"/>
          <stop offset="1" stop-color="var(--map-tint-b)"/>
        </linearGradient>
      </defs>
      <polygon points="473,360 537,299 686,281 805,205 896,107 961,0 960,360" fill="var(--banner-shade)"/>
      <g role="img" aria-label="Dotted map of the Asia Pacific region">
        <rect x="500" y="28" width="420" height="172" rx="14" fill="url(#mapTint)" opacity="0.75"/>
        <rect x="785" y="225" width="125" height="105" rx="12" fill="url(#mapTint)" opacity="0.75"/>
      </g>
      <polyline points="473,362 537,299 686,281 805,205 896,107 962,-2" fill="none" stroke="var(--chart-line)" stroke-width="6" stroke-linejoin="round"/>
      <g fill="var(--chart-line)" stroke="var(--node-ring)" stroke-width="3">
        <circle cx="537" cy="299" r="10"/>
        <circle cx="686" cy="281" r="10"/>
        <circle cx="805" cy="205" r="10"/>
        <circle cx="896" cy="107" r="10"/>
      </g>
    </svg>
    <h1 class="headline"><span class="emphasis">The Quiet</span> Harbor<br>Surge Unveiled</h1>
    <p class="subline">7 Odd Facts Hiding Behind<br>the Quiet Harbor Surge</p>
  </div>
</div>
<p class="caption large">150% of Actual Size</p>

<div class="banner-frame actual">
  <div class="banner">
    <svg class="banner-art" width="960" height="360" viewBox="0 0 960 360">
      <defs>
        <linearGradient id="mapTintSmall" x1="0" y1="0" x2="1" y2="1">
          <stop offset="0" stop-color="var(--map-tint-a)"/>
          <stop offset="1" stop-color="var(--map-tint-b)"/>
        </linearGradient>
      </defs>
      <polygon points="473,360 537,299 686,281 805,205 896,107 961,0 960,360" fill="var(--banner-shade)"/>
      <g role="img" aria-label="Dotted map of the Asia Pacific region">
        <rect x="500" y="28" width="420" height="172" rx="14" fill="url(#mapTintSmall)" opacity="0.75"/>
        <rect x="785" y="225" width="125" height="105" rx="12" fill="url(#mapTintSmall)" opacity="0.75"/>
      </g>
      <polyline points="473,362 537,299 686,281 805,205 896,107 962,-2" fill="none" stroke="var(--chart-line)" stroke-width="6" stroke-linejoin="round"/>
      <g fill="var(--chart-line)" stroke="var(--node-ring)" stroke-width="3">
        <circle cx="537" cy="299" r="10"/>
        <circle cx="686" cy="281" r="10"/>
        <circle cx="805" cy="205" r="10"/>
        <circle cx="896" cy="107" r="10"/>
      </g>
    </svg>
    <h2 class="headline"><span class="emphasis">The Quiet</span> Harbor<br>Surge Unveiled</h2>
    <p class="subline">7 Odd Facts Hiding Behind<br>the Quiet Harbor Surge</p>
  </div>
</div>
<p class="caption actual">640px by 240px</p>

</body>
</html>
```